Wedding Dried Apple Label / Name Place Card

We are looking for a simple but stylish label to be attached via string to a bag of dried apples from my family's fruit farm. The size of the label we think should be similar to the size of a business card. The packaging will be a plastic bag: 4" x 2" x 6".
We would like it to say something like:
Remy & Joss
Est. Sept 10, 2017
Dried Apple Slices
Product of Quenton Fruit Farm
________________
(We need a spot to write in the name of the person and a table number)
Our colors are also grey and navy, and would like these colors to be used.
We have uploaded a photo of the plastic bag.
Wedding

```html
<!DOCTYPE html>
<html lang="en">
<head>
<meta charset="utf-8">
<title>Remy &amp; Joss – Dried Apple Slices Label</title>
<link rel="stylesheet" href="https://fonts.googleapis.com/css2?family=Anton&family=Playfair+Display:wght@400&family=Arimo:wght@400&display=swap">
<style>
  :root {
    --navy: #00339a;
    --silver: #cccccc;
    --silver-edge: #b8bcc8;
    --paper: #ffffff;
    --frame: #111111;
  }
  html, body {
    margin: 0;
    padding: 0;
    width: 1200px;
    height: 758px;
    overflow: hidden;
    background: var(--paper);
  }
  .canvas {
    position: relative;
    width: 1200px;
    height: 758px;
    box-sizing: border-box;
    border: 2px solid var(--frame);
    background: var(--paper);
  }
  .label {
    position: absolute;
    left: 105px;
    top: 85px;
    width: 991px;
    height: 589px;
    background: var(--navy);
    outline: 1px solid var(--silver-edge);
  }
  .label__names {
    position: absolute;
    left: 120px;
    width: 760px;
    top: 20px;
    margin: 0;
    text-align: center;
    font-family: "Playfair Display", serif;
    font-weight: 400;
    font-size: 122px;
    line-height: 1;
    color: var(--silver);
    letter-spacing: 2px;
    text-shadow: 3px 2px 0 var(--navy), 4px 3px 0 var(--silver);
  }
  .label__established {
    position: absolute;
    right: 137px;
    top: 168px;
    margin: 0;
    font-family: "Arimo", Arial, sans-serif;
    font-size: 31px;
    color: var(--silver);
  }
  .label__hole {
    position: absolute;
    left: 38px;
    top: 280px;
    width: 32px;
    height: 32px;
    border-radius: 50%;
    background: var(--silver);
    box-shadow: 0 0 0 1px var(--silver-edge);
  }
  .label__product {
    position: absolute;
    left: 125px;
    width: 745px;
    top: 242px;
    margin: 0;
    text-align: center;
    font-family: "Anton", "Arial Narrow", sans-serif;
    font-size: 74px;
    line-height: 1;
    letter-spacing: 9px;
    color: var(--silver);
  }
  .label__origin {
    position: absolute;
    left: 140px;
    width: 720px;
    top: 342px;
    margin: 0;
    text-align: center;
    font-family: "Arimo", Arial, sans-serif;
    font-size: 28px;
    letter-spacing: 6.5px;
    color: var(--silver);
  }
  .label__field {
    position: absolute;
    top: 457px;
    height: 80px;
    border-radius: 10px;
    background: var(--silver);
  }
  .label__field--guest { left: 19px; width: 574px; }
  .label__field--table { left: 616px; width: 355px; }
</style>
</head>
<body>
  <main class="canvas">
    <section class="label" aria-label="Wedding favour label">
      <h1 class="label__names">Remy &amp; Joss</h1>
      <p class="label__established">Est. Sept 10, 2017</p>
      <span class="label__hole" aria-hidden="true"></span>
      <h2 class="label__product">DRIED APPLE SLICES</h2>
      <p class="label__origin">PRODUCT OF QUENTON FRUIT FARM</p>
      <div class="label__field label__field--guest" aria-label="Space for guest name"></div>
      <div class="label__field label__field--table" aria-label="Space for table number"></div>
    </section>
  </main>
</body>
</html>
```